Birch Harbor - Countertop fabricator
Need stationary, business card and T-shirt design
Birch Harbor - Countertop fabricator -
Creative Brief
Simple
Kevin Rasble
14 Larkwood Lane Syracuse, NY13099
info@birchharborny.example
www.birchharborny.example
Back of card to list materials; Granite Quatz Marble Soapstone Solid Surface

```html
<!DOCTYPE html>
<html lang="en">
<head>
<meta charset="utf-8">
<title>Birch Harbor — Stationery Set</title>
<link href="https://fonts.googleapis.com/css2?family=Jost:wght@400;500&display=swap" rel="stylesheet">
<style>
  :root{
    --backdrop:#c9cbca;
    --paper:#ffffff;
    --bronze:#7b5d2f;
    --bronze-light:#a88a5a;
    --ink:#4a4a4a;
    --stone-faint:#efece7;
    --window:#ececec;
  }
  *{box-sizing:border-box;margin:0;padding:0}
  html,body{width:1200px;height:840px;overflow:hidden}
  body{background:var(--backdrop);font-family:"Jost",sans-serif;color:var(--ink);position:relative}
  .sheet{position:absolute;background:var(--paper);overflow:hidden;box-shadow:0 1px 2px rgba(0,0,0,.12)}
  .swoosh{position:absolute;left:0;top:0;width:100%;height:34px}
  .brand{position:absolute;display:flex;align-items:center;gap:6px;color:var(--bronze);font-weight:500;white-space:nowrap}
  .brand-square{background:var(--bronze);display:block}
  .small{font-size:7px;line-height:1.4;color:var(--ink)}
  .faint-block{position:absolute;background:var(--stone-faint)}

  /* envelope front */
  .env-front{left:41px;top:96px;width:566px;height:264px}
  .env-front .brand{left:232px;top:64px;font-size:17px}
  .env-front .brand-square{width:22px;height:22px}
  .env-front .return-address{position:absolute;left:31px;top:122px;width:120px}
  .env-front .window{position:absolute;left:319px;top:144px;width:200px;height:72px;background:var(--window);border:1px solid #dcdcdc}
  .env-front .site{position:absolute;right:10px;bottom:8px;font-size:7px}

  /* envelope back */
  .env-back{left:41px;top:377px;width:566px;height:242px}
  .env-back .flap{position:absolute;left:0;top:0;width:100%;height:110px}
  .env-back .faint-block{right:0;bottom:0;width:130px;height:140px}

  /* cards */
  .card-front{left:137px;top:660px;width:216px;height:120px}
  .card-front .brand{left:14px;top:58px;font-size:11px;flex-direction:column;gap:4px;align-items:flex-start}
  .card-front .brand-square{width:16px;height:16px}
  .card-front .panel{position:absolute;left:104px;top:0;width:112px;height:100%;background:var(--bronze);color:#fff;padding:22px 10px}
  .card-front .panel .name{font-size:8.5px;font-weight:500;margin-bottom:1px}
  .card-front .panel .role{font-size:6px;margin-bottom:14px;opacity:.85}
  .card-front .panel p{font-size:6px;line-height:1.5}
  .card-back{left:360px;top:660px;width:209px;height:120px}
  .card-back .materials{position:absolute;left:50px;top:16px;font-size:6px;line-height:1.5;text-transform:uppercase;letter-spacing:.4px;color:var(--bronze)}
  .card-back .brand{left:18px;top:92px;font-size:10px}
  .card-back .brand-square{width:10px;height:10px}
  .card-back .rule{position:absolute;left:18px;top:107px;width:80px;height:1px;background:var(--bronze)}
  .card-back .faint-block{right:0;bottom:0;width:70px;height:62px}

  /* letterhead */
  .letterhead{left:655px;top:77px;width:502px;height:703px}
  .letterhead .brand{left:214px;top:52px;font-size:17px}
  .letterhead .brand-square{width:22px;height:22px}
  .letterhead .rule{position:absolute;left:78px;top:106px;width:346px;height:2px;background:var(--bronze)}
  .letterhead .faint-block{right:0;bottom:0;width:228px;height:270px}
  .letterhead .footer{position:absolute;left:0;right:0;bottom:8px;text-align:center;font-size:7px;color:var(--ink)}
  .letterhead .footer-rule{position:absolute;left:0;bottom:0;width:100%;height:3px;background:var(--bronze)}
</style>
</head>
<body>

<svg width="0" height="0" style="position:absolute" aria-hidden="true">
  <defs>
    <linearGradient id="swooshFill" x1="0" x2="1" y1="0" y2="0">
      <stop offset="0" stop-color="#7b5d2f" stop-opacity="0"/>
      <stop offset="0.55" stop-color="#a88a5a"/>
      <stop offset="1" stop-color="#7b5d2f"/>
    </linearGradient>
  </defs>
</svg>

<section class="sheet env-front">
  <svg class="swoosh" viewBox="0 0 566 34" preserveAspectRatio="none" aria-hidden="true">
    <path d="M180 0 H566 V14 C470 6 330 4 180 0 Z" fill="url(#swooshFill)"/>
  </svg>
  <div class="brand"><span class="brand-square"></span>Birch Harbor</div>
  <p class="small return-address">14 Larkwood Lane<br>Syracuse, NY13099</p>
  <div class="window"></div>
  <p class="site">www.birchharborny.example</p>
</section>

<section class="sheet env-back">
  <svg class="flap" viewBox="0 0 566 110" preserveAspectRatio="none" aria-hidden="true">
    <path d="M0 0 H566 V8 C520 40 420 96 283 104 C146 96 46 40 0 8 Z" fill="#7b5d2f"/>
  </svg>
  <div class="faint-block"></div>
</section>

<section class="sheet card-front">
  <div class="brand"><span class="brand-square"></span>Birch Harbor</div>
  <div class="panel">
    <p class="name">Kevin Rasble</p>
    <p class="role">Sales Manager</p>
    <p>T : 315-555-0142</p>
    <p>F : 315-555-0187</p>
    <p>info@birchharborny.example</p>
  </div>
</section>

<section class="sheet card-back">
  <p class="materials">Granite · Quartz · Marble<br>Soapstone · Solid Surface</p>
  <div class="brand"><span class="brand-square"></span>Birch Harbor</div>
  <div class="rule"></div>
  <div class="faint-block"></div>
</section>

<section class="sheet letterhead">
  <svg class="swoosh" viewBox="0 0 502 34" preserveAspectRatio="none" aria-hidden="true">
    <path d="M150 0 H502 V14 C420 6 290 4 150 0 Z" fill="url(#swooshFill)"/>
  </svg>
  <div class="brand"><span class="brand-square"></span>Birch Harbor</div>
  <div class="rule"></div>
  <div class="faint-block"></div>
  <p class="footer">14 Larkwood Lane, Syracuse, NY13099 &nbsp;|&nbsp; T : 315-555-0142 &nbsp;|&nbsp; F : 315-555-0187 &nbsp;|&nbsp; W : www.birchharborny.example</p>
  <div class="footer-rule"></div>
</section>

</body>
</html>
```